Kivo Commercial Cleaning is lookong for a new business card design.

A fresh new design that's professional and stylish. We need a serious upgrade to our business cards. I have included pictures of our existing ones. Our clients include professional individuals and business owners. We woupdblike something professional and upbeat. Please have fun and see what you come uo with.

Target Market(s)

Property managers, business owners, facility managers and other similar professionals

Industry/Entity Type

Janitorial

Contact Information for Business Card

Name, cell, office number, email, web address

Font styles to use
Sans Serif

Colors

Designer to choose colors to be used in the design.

Requirements
Must have
• please use the green color in our logo
Nice to have
• Bar code
Should not have
• Address

```html
<!DOCTYPE html>
<html lang="en">
<head>
<meta charset="utf-8">
<title>Kivo Commercial Cleaning – Business Card</title>
<link href="https://fonts.googleapis.com/css2?family=Open+Sans:wght@400;700&display=swap" rel="stylesheet">
<style>
  :root {
    --page: #232323;
    --card: #222226;
    --band-blue: #4374aa;
    --mark-blue: #0b5a9a;
    --accent-green: #3bb75a;
    --text-light: #ffffff;
    --rule: #d9d9d9;
  }
  * { margin: 0; padding: 0; box-sizing: border-box; }
  html, body {
    width: 1200px; height: 780px; overflow: hidden;
    background: var(--page);
    font-family: "Open Sans", Arial, sans-serif;
  }
  .sheet {
    position: relative; width: 1200px; height: 780px;
  }
  .card {
    position: absolute;
    width: 600px; height: 343px;
    border-radius: 22px;
    background: var(--card);
    overflow: hidden;
    box-shadow: 0 10px 30px rgba(0,0,0,0.55);
  }
  .card--front { left: 170px; top: 26px; }
  .card--back { left: 430px; top: 411px; }

  /* front */
  .front-band {
    position: absolute; left: 0; right: 0; top: 42px; bottom: 50px;
    background: var(--band-blue);
    display: flex; align-items: center; justify-content: center;
  }
  .front-name {
    color: var(--mark-blue);
    font-weight: 700;
    font-size: 46px;
    line-height: 1.05;
    text-align: center;
    letter-spacing: -0.5px;
  }

  /* back */
  .back-brand {
    position: absolute; left: 38px; top: 118px; width: 210px;
    color: var(--accent-green);
    font-weight: 700;
    font-size: 34px;
    line-height: 1.08;
    text-align: center;
  }
  .back-divider {
    position: absolute; left: 268px; top: 86px;
    width: 1px; height: 140px;
    background: var(--rule);
  }
  .contact {
    position: absolute; left: 300px; top: 96px;
  }
  .contact-name {
    font-weight: 700; font-size: 30px; line-height: 1.1;
    margin-bottom: 14px;
    white-space: nowrap;
  }
  .contact-name .first { color: var(--accent-green); }
  .contact-name .last { color: var(--band-blue); }
  .contact-list { list-style: none; }
  .contact-list li {
    display: flex; align-items: center; gap: 9px;
    color: var(--text-light);
    font-size: 15px; line-height: 24px;
  }
  .contact-list svg { width: 14px; height: 14px; flex: none; }
  .back-stripes {
    position: absolute; left: 0; bottom: 0; width: 600px; height: 40px;
  }
</style>
</head>
<body>
<main class="sheet">
  <section class="card card--front" aria-label="Card front">
    <div class="front-band">
      <p class="front-name">Kivo<br>Commercial Cleaning</p>
    </div>
  </section>

  <section class="card card--back" aria-label="Card back">
    <p class="back-brand">Kivo Commercial Cleaning</p>
    <div class="back-divider"></div>
    <div class="contact">
      <h1 class="contact-name"><span class="first">Dana</span> <span class="last">Whitfield</span></h1>
      <ul class="contact-list">
        <li>
          <svg viewBox="0 0 16 16" aria-hidden="true"><path fill="#3bb75a" d="M3.6 1.2l2.3 2.6-1.3 1.8c.9 2 2.3 3.5 4.4 4.5l1.8-1.3 2.6 2.3-1.3 2.4C7 13.2 2.7 8.9 1.2 3.9z"/></svg>
          (555) 014-2290
        </li>
        <li>
          <svg viewBox="0 0 16 16" aria-hidden="true"><rect x="1" y="3" width="14" height="10" rx="1" fill="#3bb75a"/><path d="M1.5 3.8L8 9l6.5-5.2" fill="none" stroke="#222226" stroke-width="1.3"/></svg>
          dana@kivocleaning.com
        </li>
        <li>
          <svg viewBox="0 0 16 16" aria-hidden="true"><circle cx="8" cy="8" r="7" fill="#3bb75a"/><path d="M1 8h14M8 1c-3 3.5-3 10.5 0 14M8 1c3 3.5 3 10.5 0 14" fill="none" stroke="#222226" stroke-width="1"/></svg>
          www.kivocleaning.com
        </li>
      </ul>
    </div>
    <svg class="back-stripes" viewBox="0 0 600 40" aria-hidden="true">
      <polygon points="392,8 600,8 600,40 424,40" fill="#4374aa"/>
      <polygon points="0,17 372,17 404,40 0,40" fill="#3bb75a"/>
    </svg>
  </section>
</main>
</body>
</html>
```